Halvorsen Partners Business Card

Halvorsen Partners Civil Construction
Marcus Halvorsen
CEO
727-518-6094
Marcus@HalvorsenSiteworks.example
www.HalvorsenSiteworks.example
Site Development
Utility Construction
Excavation
40876 County Lane 19
Cedar Hollow, FL 34690

Target Market(s)

Construction and government

Industry/Entity Type

Business

Contact Information for Business Card

I want an unique design that make a statement

Number of Pages Required

1 page

Font styles to use

Colors

Designer to choose colors to be used in the design.

Requirements
Must have
• unique design, feel free to modify or change the color of my logo.
Nice to have
• extra design features like spot UV, foil accents, color edges, unique paper, or any thing that would make my card pop.
• I like the feel of the image that I attached

```html
<!DOCTYPE html>
<html lang="en">
<head>
<meta charset="utf-8">
<title>Halvorsen Partners Business Card</title>
<link href="https://fonts.googleapis.com/css2?family=Tenor+Sans&display=swap" rel="stylesheet">
<style>
  :root {
    --backdrop: #e6e6e8;
    --card-dark: #1b1b1b;
    --card-light: #f6f6f7;
    --brand-blue: #3a4fa8;
    --brand-grey: #9a9a9c;
    --ink: #2b2b2b;
    --rule: #3a3a3a;
  }
  * { box-sizing: border-box; margin: 0; padding: 0; }
  html, body { width: 1200px; height: 900px; overflow: hidden; }
  body {
    background: var(--backdrop);
    font-family: "Tenor Sans", "Gill Sans", sans-serif;
    position: relative;
  }
  .card {
    position: absolute;
    top: 301px;
    width: 520px;
    height: 297px;
    overflow: hidden;
    box-shadow: 0 6px 18px rgba(0,0,0,0.18);
  }

  /* front */
  .card-front { left: 60px; background: var(--card-dark); }
  .front-mark {
    position: absolute; left: 38px; top: 178px;
    display: flex; align-items: center; gap: 10px;
  }
  .mark-square { width: 30px; height: 30px; border: 4px solid var(--brand-blue); flex: none; }
  .mark-name {
    color: var(--brand-grey); font-size: 15px; letter-spacing: 0.08em; text-transform: uppercase;
  }
  .services {
    position: absolute; left: 190px; top: 56px;
    font-size: 18px; text-transform: uppercase; letter-spacing: 0.02em; line-height: 1;
  }
  .service { display: flex; align-items: center; height: 30px; white-space: nowrap; }
  .service .muted { color: var(--brand-grey); margin-right: 6px; }
  .service .accent { color: var(--brand-blue); }
  .service-site { margin-left: 14px; }
  .service-utility { margin-left: 0; }
  .service-excavation { margin-left: 0; }
  .dash { height: 2px; display: inline-block; margin-right: 10px; flex: none; }
  .dash-blue { width: 46px; background: var(--brand-blue); }
  .dash-grey { width: 90px; background: var(--brand-grey); }

  /* back */
  .card-back { left: 620px; background: var(--card-light); }
  .back-brand {
    position: absolute; right: 30px; top: 34px;
    display: flex; align-items: center; gap: 10px;
  }
  .back-brand .mark-square { width: 26px; height: 26px; border-width: 3px; }
  .brand-lockup { line-height: 1.05; }
  .brand-name { color: var(--brand-blue); font-size: 21px; text-transform: uppercase; letter-spacing: 0.02em; white-space: nowrap; }
  .brand-tag { color: var(--brand-grey); font-size: 11px; text-transform: uppercase; letter-spacing: 0.28em; }
  .rule-top { position: absolute; left: 140px; right: 30px; top: 92px; height: 1px; background: var(--rule); }
  .address {
    position: absolute; right: 30px; top: 104px; text-align: right;
    color: var(--ink); font-size: 12px; line-height: 1.35; font-style: normal;
  }
  .person { position: absolute; left: 30px; top: 170px; }
  .person-name { color: var(--brand-blue); font-size: 17px; text-transform: uppercase; letter-spacing: 0.03em; }
  .person-role { color: var(--ink); font-size: 13px; margin-top: 2px; }
  .rule-bottom { position: absolute; left: 30px; width: 300px; top: 214px; height: 1px; background: var(--rule); }
  .contacts { position: absolute; left: 30px; top: 222px; list-style: none; font-size: 11.5px; color: var(--ink); }
  .contacts li { display: flex; align-items: center; gap: 8px; height: 19px; white-space: nowrap; }
  .contacts svg { width: 11px; height: 11px; fill: var(--brand-blue); flex: none; }
</style>
</head>
<body>
  <section class="card card-front" aria-label="Card front">
    <div class="front-mark">
      <span class="mark-square"></span>
      <span class="mark-name">Halvorsen Partners</span>
    </div>
    <div class="services">
      <div class="service service-site"><span class="dash dash-blue"></span><span class="muted">Site</span><span class="accent">Development</span></div>
      <div class="service service-utility"><span class="muted">Utility</span><span class="accent">Construction</span></div>
      <div class="service service-excavation"><span class="dash dash-grey"></span><span class="accent">Excavation</span></div>
    </div>
  </section>

  <section class="card card-back" aria-label="Card back">
    <div class="back-brand">
      <span class="mark-square"></span>
      <div class="brand-lockup">
        <div class="brand-name">Halvorsen Partners</div>
        <div class="brand-tag">Civil Construction</div>
      </div>
    </div>
    <div class="rule-top"></div>
    <address class="address">40876 County Lane 19<br>Cedar Hollow<br>FL 34690</address>
    <div class="person">
      <div class="person-name">Marcus Halvorsen</div>
      <div class="person-role">CEO</div>
    </div>
    <div class="rule-bottom"></div>
    <ul class="contacts">
      <li><svg viewBox="0 0 24 24" aria-hidden="true"><path d="M6.6 10.8a15.1 15.1 0 0 0 6.6 6.6l2.2-2.2c.3-.3.7-.4 1-.2 1.1.4 2.3.6 3.6.6.6 0 1 .4 1 1V20c0 .6-.4 1-1 1A17 17 0 0 1 3 4c0-.6.4-1 1-1h3.5c.6 0 1 .4 1 1 0 1.3.2 2.5.6 3.6.1.3 0 .7-.2 1z"/></svg>727-518-6094</li>
      <li><svg viewBox="0 0 24 24" aria-hidden="true"><path d="M2 5h20v14H2zm2 2v.5l8 5 8-5V7l-8 5z"/></svg>Marcus@HalvorsenSiteworks.example</li>
      <li><svg viewBox="0 0 24 24" aria-hidden="true"><path d="M12 2a10 10 0 1 0 0 20 10 10 0 0 0 0-20zm6.9 9h-3a15 15 0 0 0-1.3-5.7A8 8 0 0 1 18.9 11zM12 4c.9 1.2 1.8 3.7 1.9 7h-3.8c.1-3.3 1-5.8 1.9-7zM9.4 5.3A15 15 0 0 0 8.1 11h-3a8 8 0 0 1 4.3-5.7zM5.1 13h3a15 15 0 0 0 1.3 5.7A8 8 0 0 1 5.1 13zM12 20c-.9-1.2-1.8-3.7-1.9-7h3.8c-.1 3.3-1 5.8-1.9 7zm2.6-1.3a15 15 0 0 0 1.3-5.7h3a8 8 0 0 1-4.3 5.7z"/></svg>www.HalvorsenSiteworks.example</li>
    </ul>
  </section>
</body>
</html>
```